Tomas's Business Cards

My husband is a self employed Cabinet Maker... who contracts to Building companies and clients directly.
He installs kitchesn, designs and also completes renovations and building work.

I would like a small, FUNKY, simple but eye catching design.

It needs to incorporate the following.
Custom Cabinets / Installations / Renovations / Design

Commercial and Residential

He does not have a Website or Chatterly,
contact number is 0438 207 619 and email is tomasvelkin@quillmail.example

I would like a Grey/Silver on black, or blue covering.. I am open to colour designs?

Thank you. :-)

Target Market(s)

Building Companies
Clients
Other Trades people onsite,. to give out at job sites

Industry/Entity Type

Business

Contact Information for Business Card

Phone: 0438 207 619
Email: tomasvelkin@quillmail.example

Font styles to use
Sans Serif

Colors
0592cd
747474
474747
1b1b1b
85cae6

Requirements
Must have
• Funky, simple, eye catching design
• Would like use of Silver/Grey - and a colour that would complement this.
• Am open to ideas :-)
Nice to have
• We do not have a logo or picture, will leave this up to you if you think an image would be beneficial???
• Thank you.

```html
<!DOCTYPE html>
<html lang="en">
<head>
<meta charset="utf-8">
<title>Tomas's Business Cards</title>
<link rel="stylesheet" href="https://fonts.googleapis.com/css2?family=Jost:wght@500;600&family=Barlow:wght@400;500&display=swap">
<style>
  :root {
    --stage: #3a3735;
    --card-white: #ffffff;
    --brand-blue: #2a5cae;
    --deep-blue: #1f4fa6;
    --bright-blue: #3f8ee0;
    --ink: #1b1b1b;
    --label: #e6e6e6;
    --photo-paper: #e9ecef;
    --photo-amber: #e6a826;
  }
  * { box-sizing: border-box; margin: 0; padding: 0; }
  html, body { width: 1200px; height: 1000px; overflow: hidden; }
  body {
    background: var(--stage);
    font-family: "Barlow", "Helvetica Neue", Arial, sans-serif;
    position: relative;
  }
  .set-label {
    position: absolute; top: 58px; right: 56px;
    color: #cfcfcf; font-size: 20px;
  }
  .side-label {
    position: absolute; top: 902px;
    color: var(--label); font-size: 21px;
  }
  .side-label--front { left: 138px; }
  .side-label--back { left: 978px; }

  .card {
    position: absolute; top: 120px;
    width: 458px; height: 740px;
    border-radius: 30px; overflow: hidden;
    box-shadow: 0 6px 18px rgba(0,0,0,.45);
  }
  .card--front { left: 136px; background: var(--card-white); }
  .card--back {
    left: 620px;
    background: linear-gradient(160deg, var(--deep-blue) 0%, var(--bright-blue) 50%, var(--deep-blue) 100%);
  }

  .front__art { position: absolute; inset: 0; }
  .front__name {
    position: absolute; top: 118px; width: 100%;
    text-align: center;
    font-family: "Jost", "Futura", Arial, sans-serif;
    font-weight: 600; font-size: 37px; letter-spacing: .5px;
    color: var(--brand-blue);
  }
  .front__role {
    position: absolute; top: 164px; left: 0; width: 100%;
    display: flex; align-items: center; justify-content: center; gap: 10px;
    font-size: 25px; color: var(--ink);
  }
  .front__role::before, .front__role::after {
    content: ""; width: 66px; height: 1.5px; background: var(--ink);
  }
  .front__services {
    position: absolute; top: 230px; width: 100%;
    list-style: none; text-align: center;
    font-size: 21px; line-height: 33.5px; color: var(--ink);
  }
  .front__services .two-line { line-height: 28px; padding-top: 3px; }
  .front__contact {
    position: absolute; top: 440px; left: 86px;
    list-style: none; font-size: 20px; color: var(--ink);
  }
  .front__contact li { display: flex; align-items: center; gap: 8px; height: 31px; }
  .front__contact svg { width: 20px; height: 20px; fill: var(--brand-blue); flex: none; }

  .back__photo { position: absolute; inset: 0; }
  .back__name {
    position: absolute; top: 50%; left: 50%;
    transform: translate(-50%, -50%) rotate(60deg);
    white-space: nowrap;
    font-family: "Jost", "Futura", Arial, sans-serif;
    font-weight: 600; font-size: 52px; letter-spacing: 1px;
    color: #ffffff;
  }
</style>
</head>
<body>
  <div class="set-label">Set2</div>

  <section class="card card--front" aria-label="Card front">
    <svg class="front__art" viewBox="0 0 458 740">
      <defs>
        <linearGradient id="toolsPhoto" x1="0" y1="0" x2="1" y2="0">
          <stop offset="0" stop-color="#f1f3f5"/>
          <stop offset=".6" stop-color="var(--photo-paper)"/>
          <stop offset="1" stop-color="#e3b64a"/>
        </linearGradient>
      </defs>
      <path role="img" aria-label="Photo of building plans with a tape measure, hammer and yellow hard hat"
            d="M0 530 C120 592 300 588 458 508 L458 740 L0 740 Z" fill="url(#toolsPhoto)"/>
      <path d="M0 515 C120 577 300 573 458 493" fill="none" stroke="var(--brand-blue)" stroke-width="7"/>
    </svg>
    <h1 class="front__name">TOMAS VELKIN</h1>
    <p class="front__role">Sole Trader</p>
    <ul class="front__services">
      <li>Custom Cabinets</li>
      <li>Installations</li>
      <li>Renovations</li>
      <li class="two-line">Design Commercial<br>and Residential</li>
    </ul>
    <ul class="front__contact">
      <li>
        <svg viewBox="0 0 24 24"><path d="M6.6 10.8a15.2 15.2 0 0 0 6.6 6.6l2.2-2.2a1 1 0 0 1 1-.25 11.4 11.4 0 0 0 3.6.57 1 1 0 0 1 1 1V20a1 1 0 0 1-1 1A17 17 0 0 1 3 4a1 1 0 0 1 1-1h3.5a1 1 0 0 1 1 1c0 1.25.2 2.45.57 3.57a1 1 0 0 1-.25 1z"/></svg>
        0438 207 619
      </li>
      <li>
        <svg viewBox="0 0 24 24"><path d="M2 5h20v14H2z M2 5l10 8 10-8" fill="var(--brand-blue)" stroke="#fff" stroke-width="1.5"/></svg>
        tomasvelkin@quillmail.example
      </li>
    </ul>
  </section>

  <section class="card card--back" aria-label="Card back">
    <div class="back__photo" role="img" aria-label="Blue-toned architectural blueprint and building structure photo"></div>
    <h2 class="back__name">TOMAS VELKIN</h2>
  </section>

  <div class="side-label side-label--front">Front</div>
  <div class="side-label side-label--back">Back</div>
</body>
</html>
```